Bright Lantern Path (BRLP) Business Card - company with a mission

Note* The file attached... orange with "Bright Lantern PATH" (in CAPS) is our logo. I am also open to having the text "bright lantern path" OUTSIDE the orange round logo for business card (so yes, you may take the text out).

The info: (the following info are separate. So either you can use Martin or Beatrice for now, but that will be 2 separate cards, not together in one card. Thanks!!

Martin K Doyle
202.555.0147
martin@brightlanternpath.example
Managing Partner

Beatrice M Orr
202.555.0183
beatrice@brightlanternpath.example
Managing Partner

Our website: www.brightlanternpath.example

BRLP LLC stands for Bright Lantern Path (non profit arm is called lantern path foundation)—our business is based out of New York City and has a non-profit arm where for every bar of soap you purchase, we donate a bar (don’t want any designs that limits us to only soap). Currently working with South Africa. We want the focus to be organic/natural soap with a mission.

Looking for a clean, fresh design.

Industry/Entity Type

Non-Profit

Requirements
Must have
• Clean, fresh, refreshing. Design should not be too busy.

```html
<!DOCTYPE html>
<html lang="en">
<head>
<meta charset="utf-8">
<title>Bright Lantern Path Business Cards</title>
<link href="https://fonts.googleapis.com/css2?family=Lato:wght@300;400;700&display=swap" rel="stylesheet">
<style>
  :root {
    --backdrop: #656565;
    --card-dark: #3d3d3c;
    --card-light: #d3d2cd;
    --orange: #f2a86b;
    --ink: #3a3a3a;
    --emboss: #4c4c4b;
    --ring: #5a5a59;
  }
  * { box-sizing: border-box; margin: 0; padding: 0; }
  html, body { width: 1200px; height: 900px; overflow: hidden; }
  body {
    background: var(--backdrop);
    font-family: "Lato", Arial, sans-serif;
    position: relative;
  }
  .card {
    position: absolute;
    top: 140px;
    width: 355px;
    height: 622px;
    border-radius: 22px;
    text-align: center;
  }
  .card--front { left: 40px; background: var(--card-dark); }
  .card--info { left: 421px; background: var(--card-light); }
  .card--back { left: 800px; background: var(--card-dark); }

  .brand-mark {
    position: absolute;
    left: 50%;
    transform: translateX(-50%);
    display: flex;
    flex-direction: column;
    align-items: center;
    gap: 12px;
  }
  .brand-mark__dot { border-radius: 50%; background: var(--orange); }
  .brand-mark__name {
    font-weight: 700;
    font-size: 15px;
    letter-spacing: 2px;
    color: var(--orange);
  }
  .card--front .brand-mark { top: 250px; }
  .card--front .brand-mark__dot { width: 120px; height: 120px; }
  .card--info .brand-mark { top: 70px; }
  .card--info .brand-mark__dot { width: 110px; height: 110px; }
  .card--back .brand-mark { top: 252px; }
  .card--back .brand-mark__dot {
    width: 116px; height: 116px;
    background: var(--card-dark);
    border: 2px solid var(--ring);
  }
  .card--back .brand-mark__name { color: #8a8a88; }

  .tagline {
    position: absolute;
    left: 0; right: 0;
    bottom: 20px;
    font-weight: 700;
    font-size: 24px;
  }
  .card--front .tagline { color: var(--orange); }
  .card--back .tagline { color: var(--emboss); }

  .person {
    position: absolute;
    top: 276px;
    left: 0; right: 0;
  }
  .person__name { font-weight: 700; font-size: 19px; color: var(--ink); }
  .person__role { font-weight: 300; font-size: 14px; color: var(--orange); margin-top: 2px; }

  .contact {
    position: absolute;
    left: 0; right: 0;
    display: flex;
    flex-direction: column;
    align-items: center;
    gap: 7px;
    font-size: 15px;
    color: var(--ink);
  }
  .contact--phone { top: 353px; }
  .contact--mail { top: 424px; }
  .contact--web { top: 499px; }
  .contact__icon {
    width: 30px; height: 30px;
    border-radius: 50%;
    background: var(--orange);
    display: flex; align-items: center; justify-content: center;
  }
</style>
</head>
<body>

<section class="card card--front">
  <div class="brand-mark">
    <div class="brand-mark__dot"></div>
    <span class="brand-mark__name">BRLP</span>
  </div>
  <p class="tagline">Bright Lantern Path</p>
</section>

<section class="card card--info">
  <div class="brand-mark">
    <div class="brand-mark__dot"></div>
    <span class="brand-mark__name">BRLP</span>
  </div>
  <div class="person">
    <p class="person__name">Beatrice M Orr</p>
    <p class="person__role">Managing Partner</p>
  </div>
  <div class="contact contact--phone">
    <span class="contact__icon">
      <svg width="16" height="14" viewBox="0 0 16 14"><path d="M1 4 C1 1 15 1 15 4 L15 5 L11 5 L11 3.5 L5 3.5 L5 5 L1 5 Z" fill="#3a3a3a"/><path d="M4 6 L12 6 L14 13 L2 13 Z" fill="#3a3a3a"/><circle cx="8" cy="9.5" r="1.8" fill="#f2a86b"/></svg>
    </span>
    <span>202.555.0183</span>
  </div>
  <div class="contact contact--mail">
    <span class="contact__icon">
      <svg width="16" height="12" viewBox="0 0 16 12"><rect x="0.5" y="0.5" width="15" height="11" fill="#3a3a3a"/><path d="M1 1 L8 7 L15 1" stroke="#f2a86b" stroke-width="1.2" fill="none"/></svg>
    </span>
    <span>beatrice@brightlanternpath.example</span>
  </div>
  <div class="contact contact--web">
    <span class="contact__icon">
      <svg width="16" height="14" viewBox="0 0 16 14"><rect x="1" y="1" width="14" height="9" fill="none" stroke="#3a3a3a" stroke-width="2"/><rect x="6" y="10" width="4" height="2" fill="#3a3a3a"/><rect x="4" y="12" width="8" height="1.5" fill="#3a3a3a"/></svg>
    </span>
    <span>www.brightlanternpath.example</span>
  </div>
</section>

<section class="card card--back">
  <div class="brand-mark">
    <div class="brand-mark__dot"></div>
    <span class="brand-mark__name">BRLP</span>
  </div>
  <p class="tagline">Bright Lantern Path</p>
</section>

</body>
</html>
```